Kestrel Mobile Wellness Co

I am a Physical Therapist. I want to go to peoples homes and give them quality one on one care for their back/thoracic/neck pain. I will give them spinal mobilizations, massage and exercise. I will do all of this in the comfort of their homes. I will bring my massage table with me so I can work on their back and neck. Fee for service. Accept check and credit cards. I am an orthopaedic specialist and a Spine specialist. I will come to your door so you don't have to come to me.

working class and upper class

Massage

• Something to let the people know they will be treated special. They will get better care with me than if they were in an outpatient setting.

```html
<!DOCTYPE html>
<html lang="en">
<head>
<meta charset="utf-8">
<title>Kestrel Mobile Wellness Co — Postcard</title>
<link href="https://fonts.googleapis.com/css2?family=Quicksand:wght@300;400;500&display=swap" rel="stylesheet">
<style>
  :root {
    --page: #ffffff;
    --sea-deep: #0b5f80;
    --sea-mid: #2a93b8;
    --sea-light: #7cc6de;
    --glow: #ffffff;
    --ink: #0d3346;
    --frame-line: rgba(8, 60, 85, 0.55);
    --skin: #b98a72;
  }
  html, body {
    margin: 0;
    width: 1200px;
    height: 1000px;
    overflow: hidden;
    background: var(--page);
    font-family: "Quicksand", sans-serif;
  }
  .canvas { position: relative; width: 1200px; height: 1000px; }

  .postcard {
    position: absolute;
    left: 70px; top: 145px;
    width: 1057px; height: 740px;
    overflow: hidden;
    box-shadow: 4px 6px 8px rgba(0,0,0,0.45);
  }
  .sea-backdrop {
    position: absolute; inset: 0;
    background:
      radial-gradient(ellipse 60% 28% at 50% 50%, rgba(255,255,255,0.55), rgba(255,255,255,0) 70%),
      radial-gradient(ellipse 22% 60% at 50% 50%, rgba(255,255,255,0.35), rgba(255,255,255,0) 70%),
      linear-gradient(180deg, var(--sea-light) 0%, var(--sea-mid) 20%, var(--sea-mid) 75%, var(--sea-deep) 100%);
  }
  .center-glow {
    position: absolute;
    left: 280px; top: 150px;
    width: 500px; height: 460px;
    background: radial-gradient(circle at 50% 50%, var(--glow) 0%, rgba(255,255,255,0.85) 30%, rgba(255,255,255,0) 68%);
  }
  .inner-rule {
    position: absolute;
    left: 25px; top: 25px; right: 25px; bottom: 27px;
    border: 1.5px solid var(--frame-line);
  }

  .headline {
    position: absolute;
    left: 0; right: 0; top: 42px;
    margin: 0;
    text-align: center;
    font-weight: 300;
    font-size: 104px;
    letter-spacing: 1px;
    color: #fff;
    text-shadow: 2px 3px 3px rgba(0,40,60,0.55);
  }
  .tagline {
    position: absolute;
    left: 0; right: 0; top: 570px;
    margin: 0;
    text-align: center;
    font-weight: 400;
    font-size: 86px;
    line-height: 1;
    color: var(--ink);
    text-shadow: 1px 2px 2px rgba(255,255,255,0.35);
  }
  .website {
    position: absolute;
    left: 0; right: 0; top: 645px;
    text-align: center;
    font-weight: 300;
    font-size: 58px;
    color: #fff;
    text-shadow: 1px 2px 3px rgba(0,40,60,0.6);
  }

  .door-frame {
    position: absolute;
    left: 382px; top: 192px;
    width: 294px; height: 363px;
    border-top: 2px solid #fff;
    border-left: 2px solid #fff;
    border-right: 2px solid #fff;
    box-shadow: 0 0 6px rgba(0,0,0,0.25);
  }
  .business-card {
    position: absolute;
    left: 407px; top: 218px;
    width: 243px; height: 342px;
    background: linear-gradient(180deg, #3d9fc4 0%, #d6eef6 28%, #ffffff 45%, #ffffff 100%);
    border: 2px solid #fff;
    box-shadow: -2px 0 4px rgba(0,0,0,0.35), 2px 0 4px rgba(0,0,0,0.35);
    text-align: center;
    color: var(--ink);
  }
  .practitioner {
    margin: 18px 0 0;
    font-size: 29px;
    font-weight: 500;
  }
  .specialty {
    margin: 4px 0 0;
    font-size: 13px;
    font-weight: 500;
  }
  .photo-slot {
    position: absolute;
    left: 35px; top: 95px;
    width: 162px; height: 142px;
    background: linear-gradient(90deg, #6fb3cc 0%, #9fd0e0 22%, var(--skin) 38%, #c59a82 60%, #a9d6e4 80%, #6fb3cc 100%);
  }
  .phone {
    position: absolute; left: 0; right: 0; top: 250px;
    margin: 0;
    font-size: 28px;
    font-weight: 400;
  }
  .payment-note {
    position: absolute; left: 0; right: 0; top: 295px;
    margin: 0;
    font-size: 13px;
    font-weight: 500;
  }
</style>
</head>
<body>
<div class="canvas">
  <section class="postcard">
    <div class="sea-backdrop" role="img" aria-label="Soft blue ocean water surface"></div>
    <div class="center-glow"></div>
    <div class="inner-rule"></div>

    <h1 class="headline">Kestrel Mobile</h1>

    <div class="door-frame"></div>
    <div class="business-card">
      <p class="practitioner">Your Name</p>
      <p class="specialty">Orthopaedic &amp; Spine Specialist</p>
      <div class="photo-slot" role="img" aria-label="Photo of a patient's bare back with the spine highlighted over a blue x-ray backdrop"></div>
      <p class="phone">(000) 000-000</p>
      <p class="payment-note">Checks &amp; Credit Cards Accepted</p>
    </div>

    <h2 class="tagline">WELLNESS CO</h2>
    <div class="website">www.yourwebsite.com</div>
  </section>
</div>
</body>
</html>
```